Colorful Drive Through Car Wash Website

Design of an interactive car wash website. We're going with lively colors and a fun website. Purple and and pink colors come to mind.

The website should be a good balance between professional and fun.

Target Market(s)

Drivers that need a quick drive through car wash

Number of Pages Required

1 page

Font styles to use
Sans Serif

Colors
e34297
886aae

Requirements
Must have
• Bubbles in the design.

```html
<!DOCTYPE html>
<html lang="en">
<head>
<meta charset="utf-8">
<title>Lumora – Drive Through Car Wash</title>
<link rel="stylesheet" href="https://fonts.googleapis.com/css2?family=Open+Sans:ital,wght@0,400;0,600;0,700;1,400&display=swap">
<style>
:root{
  --purple:#886aae;
  --purple-deep:#6f4f98;
  --pink:#e34297;
  --dark:#1f1f24;
  --ink:#2a2a2e;
  --muted:#777780;
  --line:#e4e4ea;
  --light:#f5f5f8;
  --white:#ffffff;
}
*{box-sizing:border-box;margin:0;padding:0}
html,body{width:1200px;height:4580px;overflow:hidden}
body{font-family:"Open Sans",Arial,sans-serif;color:var(--ink);background:var(--white);position:relative;font-size:13px;line-height:1.6}
.abs{position:absolute}
.photo{position:absolute;display:block}
.section-title{position:absolute;left:0;width:1200px;text-align:center;font-size:24px;font-weight:700;text-transform:uppercase;color:var(--ink);letter-spacing:.5px;line-height:1.3}
.section-lead{position:absolute;left:300px;width:600px;text-align:center;font-size:12px;color:var(--ink);line-height:1.7}
.section-lead.wide{left:250px;width:700px}

/* bubbles */
.bubble{position:absolute;border-radius:50%;border:2px solid rgba(255,255,255,.45);background:radial-gradient(circle at 32% 30%,rgba(255,255,255,.55) 0%,rgba(255,255,255,.08) 35%,rgba(136,106,174,.12) 100%);pointer-events:none}
.bubble.pink{border-color:rgba(227,66,151,.5);background:radial-gradient(circle at 32% 30%,rgba(255,255,255,.5) 0%,rgba(227,66,151,.1) 45%,rgba(227,66,151,.18) 100%)}
.bubble.soft{border-color:rgba(136,106,174,.35);background:radial-gradient(circle at 32% 30%,rgba(255,255,255,.9) 0%,rgba(136,106,174,.08) 50%,rgba(136,106,174,.16) 100%)}

/* top bar */
.topbar{position:absolute;top:0;left:0;width:1200px;height:92px;background:var(--dark);color:var(--white)}
.brand{position:absolute;left:159px;top:20px;font-size:30px;font-weight:600;color:var(--purple);letter-spacing:1px;line-height:1.2}
.tagline{position:absolute;left:159px;top:58px;font-size:11px;color:#bcbcc4}
.info{position:absolute;top:26px;font-size:11px;line-height:1.5}
.info b{display:block;font-weight:700;font-size:11px}
.info span{color:#a9a9b2;font-size:10px}
.phone{position:absolute;left:778px;top:24px;line-height:1.4}
.phone small{display:block;color:#a9a9b2;font-size:10px}
.phone strong{font-size:16px;font-weight:700}
.social{position:absolute;display:flex;gap:8px}
.social i{display:block;width:28px;height:28px;border:1px solid #8d8d96;border-radius:50%}
.topbar .social{left:940px;top:28px}

/* nav */
.nav{position:absolute;top:92px;left:0;width:1200px;height:51px;background:var(--purple)}
.nav ul{list-style:none;position:absolute;left:159px;top:0;display:flex;height:51px;align-items:center}
.nav li{font-size:11px;font-weight:700;color:var(--white);margin-right:30px;text-transform:uppercase}
.quote-btn{position:absolute;left:880px;top:0;width:173px;height:51px;background:var(--pink);color:var(--white);font-size:11px;font-weight:700;display:flex;align-items:center;justify-content:center;gap:8px;text-transform:uppercase}

/* hero */
.hero{position:absolute;top:143px;left:0;width:1200px;height:522px;overflow:hidden;background:radial-gradient(circle at 30% 40%,#7b7b80 0%,#3b3b40 45%,#1c1c20 100%)}
.hero .shade{position:absolute;inset:0;background:linear-gradient(90deg,rgba(0,0,0,.1),rgba(40,20,10,.35))}
.hero-kicker{position:absolute;top:190px;left:0;width:1200px;text-align:center;color:var(--white);font-size:34px;font-weight:400;text-transform:uppercase;line-height:1.2}
.hero-title{position:absolute;top:232px;left:0;width:1200px;text-align:center;color:var(--white);font-size:38px;font-weight:700;text-transform:uppercase;line-height:1.25}
.hero-title span{background:rgba(0,0,0,.35);padding:0 10px}
.hero-sub{position:absolute;top:288px;left:0;width:1200px;text-align:center;color:#eee;font-size:15px}
.btn-outline{position:absolute;border:1px solid currentColor;font-size:11px;font-weight:700;text-transform:uppercase;display:flex;align-items:center;justify-content:center}
.hero .btn-outline{left:542px;top:335px;width:116px;height:38px;color:var(--white)}
.dots{position:absolute;left:580px;top:450px;display:flex;gap:8px}
.dots i{width:8px;height:8px;border-radius:50%;background:rgba(255,255,255,.5)}
.dots i:first-child{background:var(--white)}

/* intro */
.intro-photo{left:159px;top:748px;width:290px;height:412px;background:linear-gradient(160deg,#8c8f96,#55585f 50%,#2f3440)}
.intro-title{position:absolute;left:487px;top:735px;font-size:22px;font-weight:700;text-transform:uppercase;line-height:1.3}
.intro-text{position:absolute;left:487px;top:780px;width:566px;font-size:12px;line-height:1.7}
.feature{position:absolute;width:260px}
.feature .icon{position:absolute;left:0;top:0;width:46px;height:46px;background:var(--purple);display:flex;align-items:center;justify-content:center}
.feature .icon.ghost{background:var(--white);border:1px solid var(--line)}
.feature h4{position:absolute;left:62px;top:-2px;font-size:14px;font-weight:700}
.feature p{position:absolute;left:62px;top:22px;width:200px;font-size:10.5px;color:var(--muted);line-height:1.6}
.feature .more{position:absolute;left:62px;top:94px;font-size:10.5px;font-weight:600;white-space:nowrap}

/* service */
.service-card{position:absolute;top:1392px;width:210px;height:242px;overflow:hidden}
.service-card .label{position:absolute;left:0;bottom:0;width:100%;height:50px;background:rgba(227,66,151,.88);color:var(--white);font-size:14px;font-weight:600;display:flex;align-items:center;justify-content:center;gap:8px}
.service-card .label.plain{background:rgba(0,0,0,.45)}
.see-all{left:537px;top:1672px;width:126px;height:38px;color:var(--purple)}

/* gallery */
.gallery{position:absolute;top:1786px;left:0;width:1200px;height:596px;overflow:hidden;background:radial-gradient(ellipse at 50% 40%,#2b2d45 0%,#12131e 60%,#08080d 100%)}
.gallery .section-title{top:62px;color:var(--white)}
.gallery .section-lead{top:112px;color:#c9c9d6}
.arrows{position:absolute;left:568px;top:172px;display:flex;gap:6px}
.arrows i{width:26px;height:26px;background:#3a3a46;display:flex;align-items:center;justify-content:center}
.arrows i.on{background:var(--pink)}
.gallery-tile{top:229px;height:260px}

/* clients */
.avatar{border-radius:50%}
.quote{position:absolute;left:210px;top:2700px;width:780px;text-align:center;font-size:12px;font-style:italic;line-height:1.8;color:var(--ink)}
.client-name{position:absolute;left:0;top:2800px;width:1200px;text-align:center;font-size:13px;font-weight:700;text-transform:uppercase}
.client-role{position:absolute;left:0;top:2822px;width:1200px;text-align:center;font-size:10px;color:var(--muted)}
.carousel-arrow{position:absolute;top:2612px}

/* team */
.member{position:absolute;top:3084px;width:203px}
.member .photo{position:relative;width:203px;height:190px}
.member h5{font-size:14px;font-weight:700;margin-top:16px}
.member small{display:block;font-size:10px;color:var(--muted)}
.member .squares{display:flex;gap:6px;margin-top:18px}
.member .squares i{width:22px;height:22px;background:var(--purple)}

/* news & faq */
.news{position:absolute;top:3541px;width:205px}
.news .photo{position:relative;width:205px;height:162px}
.date{position:absolute;left:0;top:162px;width:46px;height:68px;background:var(--purple);color:var(--white);text-align:center;padding-top:6px}
.date b{display:block;font-size:20px;line-height:1.1}
.date span{font-size:10px;font-weight:700;text-transform:uppercase}
.news h6{position:absolute;left:56px;top:168px;width:150px;font-size:15px;font-weight:600;line-height:1.3}
.news .meta{position:absolute;left:56px;top:214px;font-size:9px;color:var(--muted);white-space:nowrap}
.news p{position:absolute;left:0;top:240px;width:205px;font-size:10px;color:var(--muted);line-height:1.6}
.news .more{position:absolute;left:0;top:282px;font-size:10.5px;font-weight:600}
.faq{position:absolute;left:601px;top:3548px;width:452px}
.faq-item{border:1px solid var(--line);background:var(--white);margin-bottom:12px}
.faq-item .q{height:44px;display:flex;align-items:center;justify-content:space-between;padding:0 20px;font-size:13px;font-weight:600}
.faq-item .a{padding:6px 20px 16px;font-size:10.5px;color:var(--muted);line-height:1.7;border-top:1px solid var(--line)}

/* appointment */
.appoint{position:absolute;top:3954px;left:0;width:1200px;height:574px;overflow:hidden;background:linear-gradient(100deg,#111115 0%,#1e1e24 40%,#4a4448 70%,#2a2628 100%)}
.appoint-icon{position:absolute;left:580px;top:40px;width:40px;height:40px;border-radius:50%;background:var(--purple);display:flex;align-items:center;justify-content:center}
.appoint h2{position:absolute;left:0;top:92px;width:1200px;text-align:center;color:var(--white);font-size:26px;font-weight:400;line-height:1.3}
.appoint .lead{position:absolute;left:350px;top:136px;width:500px;text-align:center;color:#d7d7dd;font-size:12px;line-height:1.7}
.form{position:absolute;left:345px;top:198px;width:516px;height:260px;background:rgba(0,0,0,.8);padding:22px 30px}
.form .row{display:flex;gap:12px}
.field{flex:1;height:32px;border:1px solid #4a4a52;color:#9a9aa3;font-size:10px;padding:8px 10px}
.field.area{height:128px;margin-top:12px}
.send{position:absolute;left:218px;top:208px;width:80px;height:30px;background:var(--pink);color:var(--white);font-size:10px;font-weight:700;display:flex;align-items:center;justify-content:center;text-transform:uppercase}

.footer{position:absolute;top:4528px;left:0;width:1200px;height:52px;background:var(--purple);color:var(--white);font-size:11px;display:flex;align-items:center;justify-content:center}
</style>
</head>
<body>

<header class="topbar">
  <div class="brand">LUMORA</div>
  <div class="tagline">Drive through car wash</div>
  <div class="info" style="left:432px"><b>EMAIL</b><span>hello@lumora.com</span></div>
  <div class="info" style="left:590px"><b>OPEN HOURS</b><span>Mon - Sat 8:00 am - 7:00 pm</span></div>
  <div class="phone"><small>Call now</small><strong>(555) 240-17-86</strong></div>
  <div class="social"><i></i><i></i><i></i><i></i></div>
</header>

<nav class="nav">
  <ul><li>Home</li><li>About Us</li><li>Service</li><li>Gallery</li><li>Testimonial</li><li>Blog</li><li>Contact Us</li></ul>
  <div class="quote-btn">
    <svg width="12" height="12" viewBox="0 0 12 12"><path d="M1 11 L11 1 M5 1 H11 V7" stroke="#fff" stroke-width="1.6" fill="none"/></svg>
    Get Free Quote
  </div>
</nav>

<section class="hero" role="img" aria-label="Photo of a car wheel being washed in a drive through wash">
  <div class="shade"></div>
  <i class="bubble" style="left:70px;top:60px;width:90px;height:90px"></i>
  <i class="bubble" style="left:180px;top:150px;width:36px;height:36px"></i>
  <i class="bubble pink" style="left:110px;top:300px;width:60px;height:60px"></i>
  <i class="bubble" style="left:960px;top:80px;width:70px;height:70px"></i>
  <i class="bubble pink" style="left:1060px;top:200px;width:44px;height:44px"></i>
  <i class="bubble" style="left:990px;top:330px;width:110px;height:110px"></i>
  <i class="bubble" style="left:880px;top:420px;width:26px;height:26px"></i>
  <div class="hero-kicker">Fine the best</div>
  <div class="hero-title"><span>Service for your car</span></div>
  <div class="hero-sub">Quick drive through wash, upfront pricing and same day service</div>
  <div class="btn-outline">Contact Now</div>
  <div class="dots"><i></i><i></i><i></i></div>
</section>

<section class="intro">
  <div class="photo intro-photo" role="img" aria-label="Photo of a car raised in a wash and service bay"></div>
  <h2 class="intro-title">Let's introduce Lumora</h2>
  <p class="intro-text">Lorem ipsum dolor sit amet, consectetur adipiscing elit. Ut lobortis lacus eget pharetra vehicula. Vestibulum in dolor facilisis sem lacinia volutpat vel sit amet est. In euismod, turpis a pharetra mattis, nisi odio ornare arcu, vitae luctus tortor diam vel quam.</p>

  <div class="feature" style="left:487px;top:888px">
    <div class="icon"><svg width="22" height="22" viewBox="0 0 22 22"><circle cx="11" cy="11" r="8" stroke="#fff" stroke-width="2" fill="none"/><circle cx="11" cy="11" r="3" fill="#fff"/></svg></div>
    <h4>Break Checkup</h4>
    <p>Lorem ipsum dolor sit amet, consectetur adipiscing elit. Ut lobortis lacus eget pharetra vehicula.</p>
    <div class="more">Read More →</div>
  </div>
  <div class="feature" style="left:787px;top:888px">
    <div class="icon ghost"><svg width="22" height="22" viewBox="0 0 22 22"><circle cx="11" cy="11" r="8" stroke="#886aae" stroke-width="1.6" fill="none"/><path d="M11 11 L15 7" stroke="#886aae" stroke-width="1.6"/></svg></div>
    <h4>Speed Metar Repair</h4>
    <p>Lorem ipsum dolor sit amet, consectetur adipiscing elit. Ut lobortis lacus eget pharetra vehicula.</p>
    <div class="more">Read More →</div>
  </div>
  <div class="feature" style="left:487px;top:1040px">
    <div class="icon ghost"><svg width="22" height="22" viewBox="0 0 22 22"><rect x="3" y="8" width="16" height="7" rx="2" stroke="#886aae" stroke-width="1.6" fill="none"/><circle cx="7" cy="16" r="2" fill="#886aae"/><circle cx="15" cy="16" r="2" fill="#886aae"/></svg></div>
    <h4>Inspection</h4>
    <p>Lorem ipsum dolor sit amet, consectetur adipiscing elit. Ut lobortis lacus eget pharetra vehicula.</p>
    <div class="more">Read More →</div>
  </div>
  <div class="feature" style="left:787px;top:1040px">
    <div class="icon ghost"><svg width="22" height="22" viewBox="0 0 22 22"><path d="M4 18 L18 4 M10 4 H18 V12" stroke="#886aae" stroke-width="1.6" fill="none"/></svg></div>
    <h4>Upgrades</h4>
    <p>Lorem ipsum dolor sit amet, consectetur adipiscing elit. Ut lobortis lacus eget pharetra vehicula.</p>
    <div class="more">Read More →</div>
  </div>
</section>

<section class="service">
  <h2 class="section-title" style="top:1248px">Our Service</h2>
  <p class="section-lead" style="top:1302px">Keeping a well-washed vehicle is paramount to your safety. That is why our team of nearly 500 professional washers are ready to make your vehicle shine and safe</p>
  <div class="service-card" style="left:159px">
    <div class="photo" style="inset:0;background:linear-gradient(150deg,#d9b36a,#8a6a3a 55%,#3a2f28)" role="img" aria-label="Photo of fresh oil being poured into an engine"></div>
    <i class="bubble" style="left:150px;top:20px;width:34px;height:34px"></i>
    <div class="label">Inspection →</div>
  </div>
  <div class="service-card" style="left:387px">
    <div class="photo" style="inset:0;background:linear-gradient(150deg,#a9b3c2,#5c6878 55%,#2c3440)" role="img" aria-label="Photo of hands washing a car with foam"></div>
    <i class="bubble" style="left:20px;top:30px;width:40px;height:40px"></i>
    <i class="bubble" style="left:150px;top:110px;width:24px;height:24px"></i>
    <div class="label">Car Cleaning →</div>
  </div>
  <div class="service-card" style="left:615px">
    <div class="photo" style="inset:0;background:linear-gradient(150deg,#b9a9a0,#7a5450 55%,#3b2a2c)" role="img" aria-label="Photo of a technician in red polishing a car"></div>
    <div class="label">Car Repair →</div>
  </div>
  <div class="service-card" style="left:843px">
    <div class="photo" style="inset:0;background:linear-gradient(150deg,#9aa3ad,#5a626c 55%,#2b3038)" role="img" aria-label="Photo of a car in a wash bay"></div>
    <div class="label plain">Upgrades →</div>
  </div>
  <div class="btn-outline abs see-all">See All Service</div>
</section>

<section class="gallery">
  <i class="bubble" style="left:60px;top:80px;width:80px;height:80px;opacity:.6"></i>
  <i class="bubble pink" style="left:150px;top:40px;width:30px;height:30px;opacity:.7"></i>
  <i class="bubble" style="left:1070px;top:60px;width:60px;height:60px;opacity:.6"></i>
  <i class="bubble pink" style="left:1090px;top:500px;width:44px;height:44px;opacity:.7"></i>
  <i class="bubble" style="left:80px;top:510px;width:36px;height:36px;opacity:.6"></i>
  <h2 class="section-title">Work Gallery</h2>
  <p class="section-lead">Phasellus ut dapibus sapien, eget volutpat nunc. Interdum et malesuada fames ac ante ipsum primis in faucibus. Vestibulum ante ipsum primis in faucibus orci luctus et ultrices.</p>
  <div class="arrows">
    <i><svg width="10" height="10" viewBox="0 0 10 10"><path d="M7 1 L3 5 L7 9" stroke="#fff" stroke-width="1.5" fill="none"/></svg></i>
    <i class="on"><svg width="10" height="10" viewBox="0 0 10 10"><path d="M3 1 L7 5 L3 9" stroke="#fff" stroke-width="1.5" fill="none"/></svg></i>
  </div>
  <div class="photo gallery-tile" style="left:159px;width:223px;background:linear-gradient(150deg,#c7c9cc,#777b80 55%,#3a3d42)" role="img" aria-label="Photo of a technician working under a car"></div>
  <div class="photo gallery-tile" style="left:382px;width:220px;background:linear-gradient(150deg,#a6a8ab,#55585c 55%,#2a2b2e)" role="img" aria-label="Photo of a technician checking an engine bay"></div>
  <div class="photo gallery-tile" style="left:602px;width:218px;background:linear-gradient(150deg,#d7d2cc,#8a7a72 55%,#3e3532)" role="img" aria-label="Photo of a technician with a tyre in the wash bay"></div>
  <div class="photo gallery-tile" style="left:820px;width:220px;background:linear-gradient(150deg,#6f87a8,#3c4f6c 55%,#1b2434)" role="img" aria-label="Photo of a gloved hand giving a thumbs up beside a clean blue car"></div>
</section>

<section class="clients">
  <i class="bubble soft" style="left:150px;top:2480px;width:70px;height:70px"></i>
  <i class="bubble soft" style="left:230px;top:2570px;width:30px;height:30px"></i>
  <i class="bubble soft" style="left:980px;top:2500px;width:56px;height:56px"></i>
  <i class="bubble soft" style="left:1010px;top:2760px;width:26px;height:26px"></i>
  <h2 class="section-title" style="top:2466px">Client's Love Us</h2>
  <p class="section-lead" style="top:2512px">Phasellus ut dapibus sapien, eget volutpat nunc. Interdum et malesuada fames ac ante ipsum primis</p>
  <svg class="carousel-arrow" style="left:414px" width="14" height="20" viewBox="0 0 14 20"><path d="M10 2 L3 10 L10 18" stroke="#555" stroke-width="1.6" fill="none"/></svg>
  <svg class="carousel-arrow" style="left:772px" width="14" height="20" viewBox="0 0 14 20"><path d="M4 2 L11 10 L4 18" stroke="#555" stroke-width="1.6" fill="none"/></svg>
  <div class="photo avatar" style="left:457px;top:2596px;width:52px;height:52px;background:linear-gradient(160deg,#c9b3a3,#6d5a50)" role="img" aria-label="Client portrait"></div>
  <div class="photo avatar" style="left:556px;top:2578px;width:88px;height:88px;background:linear-gradient(160deg,#d6bfb0,#7a5e52);box-shadow:0 0 0 4px #fff,0 2px 10px rgba(0,0,0,.2)" role="img" aria-label="Featured client portrait"></div>
  <div class="photo avatar" style="left:690px;top:2596px;width:52px;height:52px;background:linear-gradient(160deg,#cdb8ac,#6a5a54)" role="img" aria-label="Client portrait"></div>
  <p class="quote">Ut lobortis lacus eget pharetra vehicula. Vestibulum in dolor facilisis sem lacinia volutpat vel sit amet est. In euismod, turpis a pharetra mattis, nisi odio ornare arcu, vitae luctus tortor diam vel quam. Phasellus neque ipsum, efficitur vel fringilla id, congue id augue. In fringilla porta vestibulum. Phasellus ut dapibus sapien, eget volutpat nunc, interdum et malesuada fames ac.</p>
  <div class="client-name">Nadia Corvell</div>
  <div class="client-role">Happy customer</div>
</section>

<section class="team">
  <h2 class="section-title" style="top:2962px">Our Expert Team</h2>
  <p class="section-lead wide" style="top:3006px">Phasellus ut dapibus sapien, eget volutpat nunc. Interdum et malesuada fames ac ante ipsum primis in faucibus. Vestibulum ante ipsum primis in faucibus orci luctus et ultrices posuere cubilia Curae; Aliquam fermentum fringilla varius.</p>
  <div class="member" style="left:159px">
    <div class="photo" style="background:linear-gradient(160deg,#aebfd6,#5b6f8c 55%,#2f3a4c)" role="img" aria-label="Portrait of a technician with a clipboard"></div>
    <h5>Dario Venti</h5><small>Body Expert</small>
    <div class="squares"><i></i><i></i><i></i><i></i></div>
  </div>
  <div class="member" style="left:390px">
    <div class="photo" style="background:linear-gradient(160deg,#b8c4d2,#66788c 55%,#323c48)" role="img" aria-label="Portrait of a technician holding a wrench"></div>
    <h5>Marco Ellison</h5><small>Car Cleaner</small>
    <div class="squares"><i></i><i></i><i></i><i></i></div>
  </div>
  <div class="member" style="left:620px">
    <div class="photo" style="background:linear-gradient(160deg,#c2c4c8,#6e7278 55%,#34373c)" role="img" aria-label="Portrait of a technician in a cap"></div>
    <h5>Tobin Arley</h5><small>Damage Repair</small>
    <div class="squares"><i></i><i></i><i></i><i></i></div>
  </div>
  <div class="member" style="left:850px">
    <div class="photo" style="background:linear-gradient(160deg,#a8b7c8,#586a80 55%,#2b3542)" role="img" aria-label="Portrait of a technician beside a lifted car"></div>
    <h5>Felix Ormond</h5><small>Machine Master</small>
    <div class="squares"><i></i><i></i><i></i><i></i></div>
  </div>
</section>

<section class="news-faq">
  <h2 class="section-title" style="top:3410px">FAQ &amp; News</h2>
  <p class="section-lead wide" style="top:3456px">Phasellus ut dapibus sapien, eget volutpat nunc. Interdum et malesuada fames ac ante ipsum primis in faucibus. Vestibulum ante ipsum primis in faucibus orci luctus et ultrices posuere cubilia Curae; Aliquam fermentum fringilla varius.</p>
  <article class="news" style="left:159px">
    <div class="photo" style="background:linear-gradient(160deg,#c6b0a8,#7a4e4a 55%,#3a2a2a)" role="img" aria-label="Photo of a technician leaning into a car engine"></div>
    <div class="date"><b>15</b><span>Feb</span></div>
    <h6>Duis facilisis eu urna in dictum</h6>
    <div class="meta">♡ 1294 &nbsp; ◌ 13 Comments</div>
    <p>Praesent efficitur ipsum ac iaculis rutrum, sem orci tincidunt nisi, nec elementum.</p>
    <div class="more">Read More →</div>
  </article>
  <article class="news" style="left:384px">
    <div class="photo" style="background:linear-gradient(160deg,#9fb0c8,#4f607c 55%,#232c3c)" role="img" aria-label="Photo of a technician cleaning a tyre on a dark car"></div>
    <div class="date"><b>15</b><span>Feb</span></div>
    <h6>Duis facilisis eu urna in dictum</h6>
    <div class="meta">♡ 1294 &nbsp; ◌ 13 Comments</div>
    <p>Praesent efficitur ipsum ac iaculis rutrum, sem orci tincidunt nisi, nec elementum.</p>
    <div class="more">Read More →</div>
  </article>
  <div class="faq">
    <div class="faq-item">
      <div class="q">Duis facilisis eu urna in dictum
        <svg width="12" height="8" viewBox="0 0 12 8"><path d="M1 7 L6 2 L11 7" stroke="#333" stroke-width="1.5" fill="none"/></svg></div>
      <div class="a">Lorem ipsum dolor sit amet, consectetur adipiscing elit. Ut lobortis lacus eget pharetra vehicula. Vestibulum in dolor facilisis sem lacinia volutpat vel sit amet est. In euismod.</div>
    </div>
    <div class="faq-item"><div class="q">Duis facilisis eu urna in dictum<svg width="12" height="8" viewBox="0 0 12 8"><path d="M1 1 L6 6 L11 1" stroke="#333" stroke-width="1.5" fill="none"/></svg></div></div>
    <div class="faq-item"><div class="q">Duis facilisis eu urna in dictum<svg width="12" height="8" viewBox="0 0 12 8"><path d="M1 1 L6 6 L11 1" stroke="#333" stroke-width="1.5" fill="none"/></svg></div></div>
    <div class="faq-item"><div class="q">Duis facilisis eu urna in dictum<svg width="12" height="8" viewBox="0 0 12 8"><path d="M1 1 L6 6 L11 1" stroke="#333" stroke-width="1.5" fill="none"/></svg></div></div>
  </div>
</section>

<section class="appoint" role="img" aria-label="Dark wash bay photo of a technician leaning over a car">
  <i class="bubble" style="left:90px;top:70px;width:100px;height:100px;opacity:.5"></i>
  <i class="bubble pink" style="left:210px;top:200px;width:40px;height:40px;opacity:.7"></i>
  <i class="bubble" style="left:140px;top:380px;width:60px;height:60px;opacity:.5"></i>
  <i class="bubble pink" style="left:960px;top:90px;width:54px;height:54px;opacity:.7"></i>
  <i class="bubble" style="left:1010px;top:300px;width:90px;height:90px;opacity:.5"></i>
  <div class="appoint-icon"><svg width="18" height="18" viewBox="0 0 18 18"><path d="M3 15 L15 3 M8 3 H15 V10" stroke="#fff" stroke-width="1.6" fill="none"/></svg></div>
  <h2>Get Free appointment</h2>
  <p class="lead">Nunc vulputate porta dui, ut ultrices per magna varius eu. Vivamus id amet maximus risus, quis vestibulum risus. Duis facilisis eu urna in dictum.</p>
  <div class="form">
    <div class="row"><div class="field">Username</div><div class="field">Email</div><div class="field">Phone Number</div></div>
    <div class="field area">Message</div>
    <div class="send">Send</div>
  </div>
</section>

<footer class="footer">© 2013-2016 Lumora. All rights reserved.</footer>

</body>
</html>
```